Professional Business card

I need a business card to send with all my shipments. It needs to look very professional as I am branding myself, more than I am branding my company. The website is not active yet but that along with the instagram is very important as this will be moving shortly. The next required to be included is listed

Target Market(s)

All

Contact Information for Business Card

Very professional and sleek, I am trying to look like the CEO, motivational speaker and future president I plan to be

Colors
ffcf3e

Requirements
Must have
• Front

Derek Holmgren
CEO
Veltora Franchiser
Business Consultant/Start Up Guidance
Motivational Speaker
President of The United States 2040
www.derekholmgren-demo.com
[Instagram] @derekholmgren

Back
I teach the success method used by my company you just bought from. Learn the unique model and start your own Veltora franchise today
Nice to have
• Black and Gold lettering
Should not have
• Playful vibes

```html
<!DOCTYPE html>
<html lang="en">
<head>
<meta charset="UTF-8">
<title>Derek Holmgren — Business Card</title>
<link rel="stylesheet" href="https://fonts.googleapis.com/css2?family=Lato:wght@400;700;900&display=swap">
<style>
  :root {
    --gold: #ffcf3e;
    --ink: #111111;
    --card-black: #050505;
    --paper: #ffffff;
    --backdrop: #56585b;
  }
  * { box-sizing: border-box; margin: 0; padding: 0; }
  html, body {
    width: 1200px;
    height: 1000px;
    overflow: hidden;
    background: var(--backdrop);
    font-family: "Lato", sans-serif;
  }
  .stage {
    position: relative;
    width: 1200px;
    height: 1000px;
  }
  .card {
    position: absolute;
    left: 250px;
    width: 700px;
    height: 410px;
    border-radius: 34px;
  }

  /* Front: yellow face with white border */
  .card-front {
    top: 60px;
    background: var(--paper);
    padding: 26px;
  }
  .card-front .face {
    position: relative;
    width: 100%;
    height: 100%;
    background: var(--gold);
    border-radius: 26px;
    color: var(--ink);
    padding: 46px 44px 40px;
  }
  .title {
    font-weight: 900;
    font-size: 27px;
    letter-spacing: 1.2px;
    text-transform: uppercase;
  }
  .subtitle {
    margin-top: 8px;
    font-size: 17px;
    letter-spacing: 0.6px;
    padding-bottom: 10px;
    border-bottom: 1.5px solid var(--ink);
  }
  .initial { font-weight: 900; }
  .details {
    position: absolute;
    left: 44px;
    bottom: 40px;
    font-size: 17px;
    letter-spacing: 0.8px;
    line-height: 1.75;
  }
  .franchise { text-transform: uppercase; }
  .domain { font-weight: 900; }

  /* Back: black face with name */
  .card-back {
    top: 530px;
    background: var(--card-black);
    display: flex;
    flex-direction: column;
    align-items: center;
    justify-content: center;
    color: var(--gold);
  }
  .name {
    font-weight: 900;
    font-size: 58px;
    letter-spacing: 3px;
    text-transform: uppercase;
  }
  .handle {
    margin-top: 14px;
    display: flex;
    align-items: center;
    gap: 12px;
    font-size: 24px;
    letter-spacing: 0.8px;
  }
  .handle-dot { display: block; }
</style>
</head>
<body>
  <main class="stage">
    <section class="card card-front">
      <div class="face">
        <h1 class="title">President of the United States 2040</h1>
        <p class="subtitle"><span class="initial">M</span>otivational speaker</p>
        <div class="details">
          <p class="franchise"><span class="initial">V</span>eltora Franchiser</p>
          <p class="services"><span class="initial">B</span>usiness consultant / <span class="initial">S</span>tart up guidance</p>
          <p class="website">www.<span class="domain">derekholmgren-demo</span>.com</p>
        </div>
      </div>
    </section>

    <section class="card card-back">
      <h2 class="name">Derek Holmgren</h2>
      <p class="handle">
        <svg class="handle-dot" width="22" height="22" viewBox="0 0 22 22" aria-hidden="true">
          <circle cx="11" cy="11" r="10" fill="var(--gold)"/>
        </svg>
        <span>@derekholmgren</span>
      </p>
    </section>
  </main>
</body>
</html>
```